Brightway Haul & Repair Services, are a company that offers a 'one stop shop' pre-move clean up a

I have already selected a logo which I would like on the front of the business cards along with phone numbers, web address and email which are:
0419574302
www.brightwayhaul.com.au
brightwayhaulrepair@mailbox.example

On the back of the card I would like to list some of the types of service we offer (clean - move - repairs/maintenance) which are:
WASH - windows, gutters, solar panels, driveways/paths, carpets.
HAUL - Small/medium size house/office moves, large item pick-up & delivery, yard clean-up and removal.
General maintenance and repairs.

I would like the blue logo on a gray background.

Thanks

```html
<!DOCTYPE html>
<html lang="en">
<head>
<meta charset="utf-8">
<title>Brightway Haul &amp; Repair Services – Business Card</title>
<link rel="stylesheet" href="https://fonts.googleapis.com/css2?family=Arimo:wght@400;700&display=swap">
<style>
  :root {
    --page-bg: #ffffff;
    --card-bg: #e5e5e5;
    --brand-blue: #2970ff;
    --ink: #111111;
  }
  html, body {
    margin: 0;
    padding: 0;
    width: 1200px;
    height: 584px;
    overflow: hidden;
    background: var(--page-bg);
    font-family: "Arimo", Arial, Helvetica, sans-serif;
    color: var(--ink);
  }
  .canvas {
    position: relative;
    width: 1200px;
    height: 584px;
  }
  .card {
    position: absolute;
    top: 152px;
    width: 483px;
    height: 295px;
    background: var(--card-bg);
    text-align: center;
    letter-spacing: 0.04em;
    font-size: 14.5px;
    line-height: 1.1;
  }
  .card--front { left: 99px; }
  .card--back  { left: 618px; }

  /* Front */
  .brand {
    position: absolute;
    left: 0;
    right: 0;
    top: 62px;
    display: flex;
    align-items: center;
    justify-content: center;
    gap: 14px;
  }
  .brand__mark {
    width: 46px;
    height: 46px;
    flex: none;
  }
  .brand__name {
    margin: 0;
    font-weight: 700;
    font-size: 26px;
    line-height: 1.12;
    letter-spacing: 0.01em;
    color: var(--brand-blue);
    text-align: left;
  }
  .contact {
    position: absolute;
    left: 0;
    right: 0;
    top: 185px;
    margin: 0;
    font-style: normal;
  }
  .contact__line { display: block; margin-bottom: 3px; }
  .website {
    position: absolute;
    left: 0;
    right: 0;
    bottom: 4px;
    margin: 0;
  }

  /* Back */
  .services {
    position: absolute;
    left: 0;
    right: 0;
    top: 80px;
    margin: 0;
    padding: 0;
    list-style: none;
    letter-spacing: 0.03em;
  }
  .service { margin-bottom: 19px; }
  .service--general { margin-top: 22px; }
  .service__key {
    font-weight: 700;
    color: var(--brand-blue);
  }
</style>
</head>
<body>
<main class="canvas">
  <section class="card card--front" aria-label="Card front">
    <div class="brand">
      <svg class="brand__mark" viewBox="0 0 46 46" aria-hidden="true">
        <circle cx="23" cy="23" r="23" fill="var(--brand-blue)"/>
      </svg>
      <h1 class="brand__name">Brightway Haul<br>&amp; Repair Services</h1>
    </div>
    <address class="contact">
      <span class="contact__line">0419574302</span>
      <span class="contact__line">brightwayhaulrepair@mailbox.example</span>
    </address>
    <p class="website">www.brightwayhaul.com.au</p>
  </section>

  <section class="card card--back" aria-label="Card back">
    <ul class="services">
      <li class="service"><span class="service__key">WASH</span> - windows, gutters, solar panels,<br>driveways/paths, carpets.</li>
      <li class="service"><span class="service__key">HAUL</span> - Small/medium size house/office moves,<br>large item pick-up &amp; delivery, yard clean-up and removal.</li>
      <li class="service service--general">General <span class="service__key">Upkeep</span> and <span class="service__key">Repairs</span></li>
    </ul>
  </section>
</main>
</body>
</html>
```